VOSKE - New website for high-quality knives, aprons, chopping boards and caps for Grillers

We would like to develop a new website for our brand-new outdoor cooking brand VOSKE. VOSKE is a brand by grillers for grillers. Therefore the griller will always be in the centre of everything that we do. We want to appear as a cool, robust brand without being too stereotypical (like any other BBQ brands (so not too much black, red, flames)). We're very international and that should also come back in the design.

Main colour will be the yellow supported by red white and black. However, we're also open to other colours

VOSKE will be sold in-store but we want to provide more information to our clients via the website. This will be done through detailed descriptions but also blogs and downloads. We will work together with influencers to share recipes in our Pavane (magazine) and on our blog page.

Website needs to be responsive (web+mobile) and our own team should be able to easily add new content to the website.

Target Market(s)

International grillers or home chefs

Industry/Entity Type

BBQ and outdoor cooking

Coding

Coded - Design and coding required

Other font styles liked:
• Allan & Cambria

Colors

Designer to choose colors to be used in the design.

Requirements
Must have
• home, products (not shop), blog, contact, socials, downloads (for Pavane).
Nice to have
• instagram grid with #voske
Should not have
• too stereotypical BBQ website (red, flames, black)

```html
<!DOCTYPE html>
<html lang="en">
<head>
<meta charset="utf-8">
<title>VOSKE — A Brand By Grillers For Grillers</title>
<link href="https://fonts.googleapis.com/css2?family=Noto+Serif:ital,wght@0,400;0,700;1,400&family=Mulish:ital,wght@0,400;0,600;0,700;0,800;1,600&display=swap" rel="stylesheet">
<style>
:root{
  --yellow:#f6be12;
  --yellow-deep:#e8ad0c;
  --orange:#e48c0c;
  --orange-light:#d9a31e;
  --dark:#1f1f1f;
  --dark-2:#262626;
  --ink:#222222;
  --muted:#555555;
  --white:#ffffff;
  --grey-bg:#f2f2f2;
  --card-border:#c9c9c9;
}
*{margin:0;padding:0;box-sizing:border-box}
html,body{width:1200px;height:4902px;overflow:hidden}
body{font-family:"Mulish",Arial,sans-serif;color:var(--ink);background:var(--white);position:relative}
.serif{font-family:"Noto Serif",Georgia,serif}
section,header,footer,nav{position:absolute;left:0;width:1200px}
.btn{position:absolute;display:flex;align-items:center;justify-content:center;background:var(--yellow);color:var(--white);font-weight:800;font-size:13px;letter-spacing:.5px;border-radius:24px;text-transform:uppercase}
.photo{position:absolute}

/* top bar */
.topbar{top:0;height:34px;background:var(--dark);z-index:4}
.topbar span{position:absolute;top:9px;font-size:12px;color:var(--yellow);display:flex;align-items:center;gap:7px}
/* nav */
.nav{top:34px;height:61px;background:var(--white);z-index:6}
.nav a{position:absolute;top:21px;font-size:14px;font-weight:700;color:var(--ink);text-decoration:none;transform:translateX(-50%)}
.brand-badge{position:absolute;left:539px;top:-34px;width:122px;height:122px;border-radius:50%;background:var(--white);display:flex;align-items:center;justify-content:center;z-index:7}
.brand-badge .disc{width:96px;height:96px;border-radius:50%;background:var(--yellow);display:flex;align-items:center;justify-content:center;color:var(--white);font-family:"Noto Serif",Georgia,serif;font-weight:700;font-size:21px;letter-spacing:1px}

/* hero */
.hero{top:95px;height:542px;z-index:1}
.hero .photo{inset:0;background:radial-gradient(ellipse at 30% 60%,#5a4a38 0%,#2f2a24 45%,#1b1a18 100%)}
.hero .shade{position:absolute;inset:0;background:rgba(0,0,0,.25)}
.hero .tagline{position:absolute;top:96px;width:100%;text-align:center;color:var(--white);font-size:28px}
.hero h1{position:absolute;top:130px;width:100%;text-align:center;color:var(--white);font-size:118px;font-weight:700;letter-spacing:4px;line-height:1.15}
.hero p{position:absolute;top:277px;left:270px;width:660px;text-align:center;color:var(--white);font-size:20px;line-height:30px}
.hero .arrow{position:absolute;top:240px}
.hero .down{position:absolute;left:584px;top:513px;width:32px;height:32px;border-radius:50%;background:var(--yellow);display:flex;align-items:center;justify-content:center}

/* about */
.about{top:637px;height:529px}
.about h2{position:absolute;left:158px;top:108px;font-size:40px;font-weight:700}
.sub-yellow{color:var(--yellow-deep);font-weight:700;font-size:21px;line-height:30px}
.body-text{font-size:13.5px;line-height:22px;color:var(--ink)}
.about .sub-yellow{position:absolute;left:158px;top:166px;width:400px}
.about .body-text{position:absolute;left:158px;top:270px;width:380px}
.about .contact-label{position:absolute;left:158px;top:352px;font-size:14px}
.about .contact-num{position:absolute;left:158px;top:374px;font-size:14px;font-weight:800}
.about .rule{position:absolute;left:158px;top:403px;width:62px;height:3px;background:var(--yellow)}
.about .ring{position:absolute;left:602px;top:39px;width:444px;height:444px;border-radius:50%;border:5px solid var(--yellow)}
.about .photo{left:608px;top:45px;width:432px;height:432px;border-radius:50%;background:linear-gradient(160deg,#5f7c46 0%,#3f5a34 50%,#6a4a34 100%)}

/* products */
.products{top:1166px;height:670px}
.dark-bg{position:absolute;inset:0}
.products h2{position:absolute;top:116px;width:100%;text-align:center;color:var(--white);font-size:36px;font-weight:700}
.product-card{position:absolute;top:192px;width:209px;height:316px;background:var(--yellow-deep)}
.product-card .photo{left:0;top:0;width:209px;height:150px}
.product-card h3{position:absolute;top:170px;width:100%;text-align:center;color:var(--white);font-size:17px;line-height:22px;font-weight:700}
.product-card p{position:absolute;top:228px;left:28px;width:153px;text-align:center;color:#4a3500;font-size:12.5px;line-height:17px}

/* magazine */
.magazine{top:1836px;height:570px}
.magazine h2{position:absolute;left:158px;top:140px;font-size:40px;font-weight:700}
.magazine .sub-yellow{position:absolute;left:158px;top:210px;width:460px;line-height:33px}
.magazine .body-text{position:absolute;left:158px;top:286px;width:440px}
.magazine .frame{position:absolute;left:683px;top:74px;width:362px;height:426px;border:2px solid #b8b8b8;background:linear-gradient(135deg,#6b4a2c 0%,#2f6fb0 40%,#1e57a0 70%,#5a3a20 100%)}

/* testimonial */
.testimonial{top:2406px;height:619px}
.testimonial h2{position:absolute;top:64px;width:100%;text-align:center;color:var(--white);font-size:38px;font-weight:700}
.testimonial .ring{position:absolute;left:160px;top:148px;width:392px;height:392px;border-radius:50%;border:6px solid var(--yellow)}
.testimonial .photo{left:166px;top:149px;width:380px;height:380px;border-radius:50%;background:linear-gradient(140deg,#3c4a52 0%,#6d7f88 45%,#8a6a46 100%)}
.quote-box{position:absolute;left:552px;top:162px;width:490px;height:350px;border:2px solid rgba(255,255,255,.85)}
.quote-box .mark{position:absolute;left:34px;top:40px}
.quote-box blockquote{position:absolute;left:32px;top:88px;width:430px;color:var(--white);font-style:italic;font-weight:600;font-size:17.5px;line-height:26px}
.quote-box .rule{position:absolute;left:32px;top:184px;width:56px;height:3px;background:var(--white)}
.quote-box .name{position:absolute;left:32px;top:208px;color:var(--white);font-weight:800;font-size:19px;letter-spacing:.5px}
.quote-box .role{position:absolute;left:32px;top:240px;color:rgba(255,255,255,.85);font-size:12px;letter-spacing:1px}
.quote-box .nav-arrows{position:absolute;left:32px;top:286px}

/* blog */
.blog{top:3025px;height:636px}
.blog h2{position:absolute;top:50px;width:100%;text-align:center;font-size:38px;font-weight:700}
.post-card{position:absolute;top:119px;width:285px;height:361px;border:2px solid var(--card-border);background:var(--white)}
.post-card .photo{left:0;top:0;width:281px;height:160px}
.post-card .date{position:absolute;left:102px;top:178px;width:77px;height:22px;border-radius:11px;background:var(--yellow);color:var(--white);font-size:12.5px;font-weight:800;display:flex;align-items:center;justify-content:center}
.post-card p{position:absolute;left:22px;top:212px;width:237px;text-align:center;font-size:14px;line-height:20px}
.post-card .more{position:absolute;top:305px;width:100%;text-align:center;font-size:13.5px;font-weight:800}
.post-card .rule{position:absolute;left:122px;top:327px;width:40px;height:3px;background:var(--yellow)}

/* instagram */
.insta{top:3661px;height:634px;background:var(--grey-bg)}
.insta h2{position:absolute;top:58px;width:100%;text-align:center;font-size:38px;font-weight:700}
.insta-grid{position:absolute;left:158px;top:141px;width:884px;height:392px;display:grid;grid-template-columns:repeat(5,1fr);grid-template-rows:repeat(2,1fr)}
.insta-grid div{border-top:4px solid var(--yellow)}

/* footer */
.footer{top:4295px;height:607px}
.footer .logo{position:absolute;left:158px;top:178px;width:90px;height:90px;border-radius:50%;background:var(--yellow);display:flex;align-items:center;justify-content:center;color:var(--white);font-family:"Noto Serif",Georgia,serif;font-weight:700;font-size:18px;letter-spacing:1px}
.footer .field{position:absolute;left:158px;top:280px;width:171px;height:38px;border-radius:19px;background:var(--white);color:#444;font-size:12px;display:flex;align-items:center;justify-content:center}
.footer .col{position:absolute;top:180px}
.footer .col h4{color:var(--yellow);font-size:14px;font-weight:600;margin-bottom:18px}
.footer .col li{list-style:none;color:var(--white);font-size:13px;line-height:16px;margin-bottom:16px}
.footer .contact-row{display:flex;gap:14px;color:var(--white);font-size:13px;line-height:18px;margin-bottom:14px}
.footer .social{position:absolute;top:426px;width:40px;height:40px;border-radius:50%;border:1.5px solid rgba(255,255,255,.7)}
.footer .copy{position:absolute;top:519px;width:100%;text-align:center;color:var(--white);font-size:13px}
.footer .copy b{color:var(--yellow);font-weight:400}
</style>
</head>
<body>

<header class="topbar">
  <span style="left:158px">
    <svg width="10" height="13" viewBox="0 0 10 13"><path d="M5 0C2.2 0 0 2.2 0 5c0 3.6 5 8 5 8s5-4.4 5-8C10 2.2 7.8 0 5 0z" fill="#f6be12"/><circle cx="5" cy="5" r="2" fill="#1f1f1f"/></svg>
    Harbour Lot Studios
  </span>
  <span style="right:158px">
    <svg width="12" height="12" viewBox="0 0 12 12"><path d="M2.4 0.5L4.3 2.6 3.3 4.3c.8 1.7 2.2 3.1 3.9 3.9l1.7-1 2.1 1.9-.9 2.3C5 11.2.8 7 .1 1.4z" fill="#f6be12"/></svg>
    1300 555 014
  </span>
</header>

<nav class="nav">
  <a style="left:232px">HOME</a>
  <a style="left:418px">PRODUCTS</a>
  <div class="brand-badge"><div class="disc">VOSKE</div></div>
  <a style="left:799px">BLOG</a>
  <a style="left:976px">CONTACT</a>
</nav>

<section class="hero">
  <div class="photo" role="img" aria-label="Griller slicing vegetables on a wooden board beside sauce bottles at an outdoor grill"></div>
  <div class="shade"></div>
  <div class="tagline serif">A Brand By Grillers For Grillers</div>
  <h1 class="serif">VOSKE</h1>
  <p>Many desktop publishing packages and web page editors now use Lorem Ipsum as their default model text</p>
  <div class="btn" style="left:525px;top:362px;width:150px;height:42px">Contact Us</div>
  <svg class="arrow" style="left:156px" width="18" height="28" viewBox="0 0 18 28"><path d="M15 2L4 14l11 12" stroke="#fff" stroke-width="4" fill="none"/></svg>
  <svg class="arrow" style="left:1026px" width="18" height="28" viewBox="0 0 18 28"><path d="M3 2l11 12L3 26" stroke="#fff" stroke-width="4" fill="none"/></svg>
  <div class="down"><svg width="14" height="16" viewBox="0 0 14 16"><path d="M7 1v13M2 9l5 5 5-5" stroke="#1f1f1f" stroke-width="2" fill="none"/></svg></div>
</section>

<section class="about">
  <h2 class="serif">About</h2>
  <div class="sub-yellow serif">Contrary to popular belief, Lorem Ipsum is not simply random text. It has roots in a piece .</div>
  <p class="body-text">There are many variations of passages of Lorem Ipsum available, but the majority have suffered alteration in some form, by injected humour,</p>
  <div class="contact-label">Contact Us</div>
  <div class="contact-num">1 800 555 0190</div>
  <div class="rule"></div>
  <div class="ring"></div>
  <div class="photo" role="img" aria-label="Griller seasoning food on a round steel fire pit grill in a garden"></div>
</section>

<section class="products">
  <svg class="dark-bg" width="1200" height="670" viewBox="0 0 1200 670"><polygon points="0,26 330,0 870,0 1200,26 1200,670 0,670" fill="#212121"/></svg>
  <h2 class="serif">Our Products</h2>
  <article class="product-card" style="left:158px"><div class="photo" role="img" aria-label="Canvas knife roll with three knives" style="background:linear-gradient(180deg,#2f4a6a,#8a8e92)"></div><h3 class="serif">High-Quality<br>Knives</h3><p>There are many variations of passages of Lorem Ipsum .</p></article>
  <article class="product-card" style="left:382px"><div class="photo" role="img" aria-label="Dark grilling apron with leather badge" style="background:linear-gradient(180deg,#3a3a3a,#1e1e1e)"></div><h3 class="serif">High-Quality<br>Aprons</h3><p>There are many variations of passages of Lorem Ipsum .</p></article>
  <article class="product-card" style="left:606px"><div class="photo" role="img" aria-label="Rolled canvas pouch on a wooden chopping board" style="background:linear-gradient(180deg,#2c4660,#a07848)"></div><h3 class="serif">High-Quality<br>Chopping Boards</h3><p>There are many variations of passages of Lorem Ipsum .</p></article>
  <article class="product-card" style="left:830px"><div class="photo" role="img" aria-label="Yellow and dark caps held in hand" style="background:linear-gradient(180deg,#d8d4cc,#3a3a3a)"></div><h3 class="serif">High-Quality<br>Caps</h3><p>There are many variations of passages of Lorem Ipsum .</p></article>
  <div class="btn" style="left:515px;top:547px;width:170px;height:46px">View Products</div>
</section>

<section class="magazine">
  <h2 class="serif">Our Pavane (Magazine)</h2>
  <div class="sub-yellow serif">Contrary to popular belief, Lorem Ipsum is not simply random text.</div>
  <p class="body-text">There are many variations of passages of Lorem Ipsum available, but the majority have suffered alteration in some form, by injected humour, or randomised</p>
  <div class="btn" style="left:158px;top:378px;width:171px;height:44px">Download Now</div>
  <div class="frame" role="img" aria-label="Stack of cooking magazines on a patterned wooden table"></div>
</section>

<section class="testimonial">
  <svg class="dark-bg" width="1200" height="619" viewBox="0 0 1200 619">
    <defs><linearGradient id="warm" x1="0" x2="1" y1="0" y2="0"><stop offset="0" stop-color="#e48c0c"/><stop offset="1" stop-color="#d9a31e"/></linearGradient></defs>
    <polygon points="0,0 1200,0 1200,619 620,559 580,559 0,619" fill="url(#warm)"/>
  </svg>
  <h2 class="serif">Client Testimonial</h2>
  <div class="ring"></div>
  <div class="photo" role="img" aria-label="Two friends smiling at an outdoor table with bread and sauces"></div>
  <div class="quote-box">
    <svg class="mark" width="40" height="30" viewBox="0 0 40 30"><path d="M2 0h14v14l-6 16H3l5-14H2zM24 0h14v14l-6 16h-7l5-14h-6z" fill="#fff"/></svg>
    <blockquote>There are many variations of passages of Lorem Ipsum available, but the majority have suffered alteration in some form, by injected humour,</blockquote>
    <div class="rule"></div>
    <div class="name">- JAMES DALE</div>
    <div class="role">Businessman</div>
    <svg class="nav-arrows" width="36" height="16" viewBox="0 0 36 16"><path d="M9 2L3 8l6 6M27 2l6 6-6 6" stroke="#fff" stroke-width="2.5" fill="none"/></svg>
  </div>
</section>

<section class="blog">
  <h2 class="serif">Blog</h2>
  <article class="post-card" style="left:158px"><div class="photo" role="img" aria-label="Hands slicing food on a board beside a spice jar" style="background:linear-gradient(160deg,#567a3c,#3a3a3a 60%,#c8c0b0)"></div><div class="date">23.09.21</div><p>There are many variations of passages of Lorem Ipsum available, but the majority have suffered .</p><div class="more">READ MORE</div><div class="rule"></div></article>
  <article class="post-card" style="left:458px"><div class="photo" role="img" aria-label="Group dining at a long outdoor garden table" style="background:linear-gradient(160deg,#6a8a4c,#4a5a40 60%,#8a7a66)"></div><div class="date">23.09.21</div><p>There are many variations of passages of Lorem Ipsum available, but the majority have suffered .</p><div class="more">READ MORE</div><div class="rule"></div></article>
  <article class="post-card" style="left:757px"><div class="photo" role="img" aria-label="Griller opening a dark kettle grill outdoors" style="background:linear-gradient(160deg,#4a6a3a,#2a3a4a 60%,#6a8a5a)"></div><div class="date">23.09.21</div><p>There are many variations of passages of Lorem Ipsum available, but the majority have suffered .</p><div class="more">READ MORE</div><div class="rule"></div></article>
  <div class="btn" style="left:515px;top:511px;width:170px;height:46px">View All</div>
</section>

<section class="insta">
  <h2 class="serif">#voske</h2>
  <div class="insta-grid">
    <div role="img" aria-label="Cream cap with yellow patch" style="background:linear-gradient(160deg,#e8e4dc,#8a7a60)"></div>
    <div role="img" aria-label="Griller at a grill wearing an apron" style="background:linear-gradient(160deg,#6a8a5a,#2e2e2e)"></div>
    <div role="img" aria-label="Friends at an outdoor dinner table" style="background:linear-gradient(160deg,#5a7a4a,#8a7060)"></div>
    <div role="img" aria-label="Blue ceramic kamado grill" style="background:linear-gradient(160deg,#3a5a7a,#1e3a5a)"></div>
    <div role="img" aria-label="Garden plants and grill in the evening" style="background:linear-gradient(160deg,#3a5a2e,#c0702a)"></div>
    <div role="img" aria-label="Sauce bottles and vegetables on a table" style="background:linear-gradient(160deg,#a03a3a,#5a7a3a)"></div>
    <div role="img" aria-label="Close view of a dark grill lid" style="background:linear-gradient(160deg,#2e2e2e,#5a4a2a)"></div>
    <div role="img" aria-label="Griller pouring at a fire pit" style="background:linear-gradient(160deg,#5a6a7a,#3a2a22)"></div>
    <div role="img" aria-label="Guests eating at a long garden table" style="background:linear-gradient(160deg,#5a7a4a,#a08a70)"></div>
    <div role="img" aria-label="Dark canvas cap with leather patch" style="background:linear-gradient(160deg,#3a3a3a,#6a4a30)"></div>
  </div>
</section>

<footer class="footer">
  <svg class="dark-bg" width="1200" height="607" viewBox="0 0 1200 607"><rect width="1200" height="607" fill="#1f1f1f"/><polygon points="0,0 1200,0 620,42 580,42" fill="#f2f2f2"/></svg>
  <div class="logo">VOSKE</div>
  <div class="field">Enter Your Mail ID</div>
  <div class="btn" style="left:158px;top:329px;width:171px;height:38px">Subscribe Now</div>
  <div class="col" style="left:375px"><h4>Quick Link</h4><ul><li>Home</li><li>Products</li><li>Blog</li><li>Contact</li></ul></div>
  <div class="col" style="left:498px"><h4>Products</h4><ul><li>Knives</li><li>Aprons</li><li>Chopping Boards</li><li>Grill Caps</li></ul></div>
  <div class="col" style="left:660px"><h4>Opening Hour</h4><ul><li>Mon - Fri :<br>10.00am - 5.00pm</li><li>Sat &amp; Sun :<br>10.00am - 10 pm</li></ul></div>
  <div class="col" style="left:816px"><h4>Contact Us</h4>
    <div class="contact-row"><svg width="12" height="16" viewBox="0 0 10 13"><path d="M5 0C2.2 0 0 2.2 0 5c0 3.6 5 8 5 8s5-4.4 5-8C10 2.2 7.8 0 5 0z" fill="#f6be12"/><circle cx="5" cy="5" r="2" fill="#1f1f1f"/></svg><span>Building 23c<br>Harbour Lot Studios<br>14 Kestrel Avenue, Lindale Park</span></div>
    <div class="contact-row"><svg width="12" height="12" viewBox="0 0 12 12"><path d="M2.4 0.5L4.3 2.6 3.3 4.3c.8 1.7 2.2 3.1 3.9 3.9l1.7-1 2.1 1.9-.9 2.3C5 11.2.8 7 .1 1.4z" fill="#f6be12"/></svg><span>1300 555 014</span></div>
    <div class="contact-row"><svg width="12" height="10" viewBox="0 0 12 10"><rect width="12" height="10" fill="#f6be12"/><path d="M0 0l6 5 6-5" stroke="#1f1f1f" fill="none"/></svg><span>www.voske.example</span></div>
  </div>
  <div class="social" style="left:507px" aria-label="Social link"></div>
  <div class="social" style="left:554px" aria-label="Social link"></div>
  <div class="social" style="left:604px" aria-label="Social link"></div>
  <div class="social" style="left:651px" aria-label="Social link"></div>
  <div class="copy">© 2021 <b>voske</b>. All rights reserved.</div>
</footer>

</body>
</html>
```